Label design/Graphic design required to brand wall paints

Would like to design a paint drum label/graphic to brand paint drums. The product is wall paints which come in plastic containers. (Refer attached pics). I have also attached the logo font. The one in the pictures are a bit too plan - need some color and creativity - not something too jazzy. You can change the icons if you wish to for the Low VOC, Washable & Eco Friendly - or keep the same. Need to incorporate the drum size "20 L" or "20 Ltr." at the bottom of the label.Rest of the matter to be incorporated is as per the content in the sample labels provided. Size of the label can be 230 x 230mm W X H.

Target Market(s)

Buildings Houses

Industry/Entity Type

Painting And Decorating

Colors

Designer to choose colors to be used in the design.

Requirements
Must have
• The content on the label samples given. Must maintain the logo font.
Nice to have
• A little more color -not jazzy. Can try giving color accents to the font if it helps.
Should not have
• Should not be cluttered.

```html
<!DOCTYPE html>
<html lang="en">
<head>
<meta charset="utf-8">
<title>Everlayer Paints – 20 Ltr. Drum Label</title>
<link rel="stylesheet" href="https://fonts.googleapis.com/css2?family=Montserrat:wght@500;700&family=Roboto:wght@700&display=swap">
<style>
  :root {
    --page: #ffffff;
    --navy: #25364f;
    --slate: #6f7b8b;
    --blue-deep: #2c78b8;
    --blue: #3a93d4;
    --blue-light: #7cb8e2;
    --band: #ffffff;
    --band-text: #2b82c4;
    --title: #ffffff;
    --tagline: #e3e8ee;
    --badge: #25364f;
    --badge-ring: #ffffff;
  }
  * { margin: 0; padding: 0; box-sizing: border-box; }
  html, body {
    width: 1200px;
    height: 1195px;
    overflow: hidden;
    background: var(--page);
  }
  .label {
    position: absolute;
    left: 240px;
    top: 205px;
    width: 720px;
    height: 785px;
    overflow: hidden;
    background: linear-gradient(180deg, var(--navy) 0%, var(--navy) 35%, var(--slate) 100%);
  }
  .label__art {
    position: absolute;
    inset: 0;
    width: 100%;
    height: 100%;
  }
  .label__band {
    position: absolute;
    left: 0;
    top: 58px;
    width: 100%;
    height: 32px;
    background: var(--band);
    display: flex;
    align-items: center;
    justify-content: center;
    font-family: "Montserrat", sans-serif;
    font-weight: 700;
    font-size: 23px;
    letter-spacing: 4px;
    color: var(--band-text);
  }
  .brand {
    position: absolute;
    left: 0;
    top: 300px;
    width: 100%;
    text-align: center;
    font-family: "Montserrat", sans-serif;
    font-weight: 700;
    font-size: 58px;
    letter-spacing: 1px;
    line-height: 1;
    color: var(--title);
  }
  .tagline {
    position: absolute;
    left: 0;
    top: 420px;
    width: 100%;
    text-align: center;
    font-family: "Montserrat", sans-serif;
    font-weight: 500;
    font-size: 28px;
    letter-spacing: 3px;
    color: var(--tagline);
  }
  .volume {
    position: absolute;
    left: 60px;
    top: 688px;
    font-family: "Roboto", sans-serif;
    font-weight: 700;
    font-size: 32px;
    color: var(--title);
  }
  .feature {
    position: absolute;
    top: 662px;
    width: 92px;
    height: 92px;
    border-radius: 50%;
    background: var(--badge);
    border: 3px solid var(--badge-ring);
    box-shadow: inset 0 0 0 10px var(--badge), inset 0 0 0 12px var(--badge-ring);
  }
  .feature--low-voc { left: 362px; }
  .feature--washable { left: 498px; }
  .feature--eco { left: 622px; }
</style>
</head>
<body>
  <section class="label" aria-label="Everlayer Paints drum label">
    <svg class="label__art" viewBox="0 0 720 785" aria-hidden="true">
      <circle cx="930" cy="560" r="620" fill="var(--blue-deep)" opacity="0.9"/>
      <circle cx="900" cy="300" r="520" fill="var(--blue)" opacity="0.75"/>
      <circle cx="520" cy="640" r="360" fill="var(--blue-light)" opacity="0.55"/>
    </svg>

    <div class="label__band">A ONE COAT APPLICATION</div>

    <h1 class="brand">EVERLAYER PAINTS</h1>

    <p class="tagline">PAINT AND PRIMER IN ONE</p>

    <p class="volume">20 Ltr.</p>

    <span class="feature feature--low-voc" role="img" aria-label="Low VOC formula badge"></span>
    <span class="feature feature--washable" role="img" aria-label="Washable badge"></span>
    <span class="feature feature--eco" role="img" aria-label="Eco friendly badge"></span>
  </section>
</body>
</html>
```